sydney wedding photography business needs a business card design

we need a business card design for a sydney based wedding photography and videography business. our business name is :golden hour studios and film. our target clients are 24-35 yrs female. our style is candid, organic, natural, dynamic. we are a team of young photographers and videographers, and help brides to create memories that they will cherish for the rest of their lives. the logo will be provided. we want an elegant design that reflects our style, and also want to give a great impression to our clients that we are one of the best studios in sydney and our brand means quality and premium service.

Target Market(s)

bride to be, 24-35 years old, living in sydney and surrunding areas

Industry/Entity Type

Wedding Photography

Contact Information for Business Card

address: 47 marrowbank street, ashcombe vale
mobile: 0417283951
phone: (02) 9163 2748
info@goldenhourstudio.net.au
www.goldenhourstudio.net.au
facebook:goldenhourbridals
instagram:goldenhourbridals

Font styles to use
Serif
Sans Serif

Requirements
Nice to have
• maybe add my slogan"moments held forever" if the layout looks good
Should not have
• no black color, not good idea for wedding biz card

```html
<!DOCTYPE html>
<html lang="en">
<head>
<meta charset="utf-8">
<title>Golden Hour Studios and Film – Business Card</title>
<link href="https://fonts.googleapis.com/css2?family=Open+Sans:wght@300;400&family=Sofia&display=swap" rel="stylesheet">
<style>
  :root {
    --sage: #a3a69e;
    --paper: #ffffff;
    --gold-deep: #b9862a;
    --gold-bright: #e3b22a;
    --gold-text: #b98a2e;
    --ink: #262626;
    --light-text: #ffffff;
  }
  * { margin: 0; padding: 0; box-sizing: border-box; }
  html, body {
    width: 1200px;
    height: 804px;
    overflow: hidden;
    background: var(--paper);
  }
  .card {
    position: relative;
    width: 1200px;
    height: 804px;
    background: var(--paper);
    font-family: "Open Sans", Arial, sans-serif;
    font-weight: 300;
  }
  .contact-band {
    position: absolute;
    left: 0; top: 0;
    width: 1200px;
    height: 402px;
    background: var(--sage);
  }
  .contact-line {
    position: absolute;
    left: 0;
    width: 100%;
    text-align: center;
    color: var(--light-text);
    font-size: 31px;
    letter-spacing: 2.2px;
    line-height: 1;
    font-weight: 400;
  }
  .contact-line.address { top: 152px; }
  .contact-line.phones  { top: 213px; }
  .contact-line.email   { top: 274px; }
  .contact-line .divider { margin: 0 18px; }
  .gold-rule {
    position: absolute;
    left: 0;
    width: 100%;
    height: 7px;
    background: linear-gradient(90deg, var(--gold-deep), var(--gold-bright));
  }
  .gold-rule.upper { top: 402px; }
  .gold-rule.lower { top: 508px; background: linear-gradient(90deg, var(--gold-bright), var(--gold-deep)); }
  .slogan {
    position: absolute;
    left: 0; top: 431px;
    width: 100%;
    text-align: center;
    font-family: "Sofia", cursive;
    font-size: 40px;
    letter-spacing: 4px;
    word-spacing: 12px;
    color: var(--gold-text);
    line-height: 1.1;
  }
  .social-row {
    position: absolute;
    left: 0; top: 610px;
    width: 100%;
    display: flex;
    justify-content: center;
    gap: 70px;
  }
  .social-item {
    display: flex;
    align-items: center;
    gap: 14px;
    color: var(--ink);
    font-size: 33px;
    line-height: 1;
  }
  .social-dot { width: 52px; height: 52px; display: block; }
  .website {
    position: absolute;
    left: 0; top: 676px;
    width: 100%;
    text-align: center;
    color: var(--ink);
    font-size: 33px;
    line-height: 1;
  }
</style>
</head>
<body>
  <div class="card">
    <section class="contact-band">
      <p class="contact-line address">47 Marrowbank St, Ashcombe Vale</p>
      <p class="contact-line phones">m 0417283951<span class="divider">I</span>p (02) 9163 2748</p>
      <p class="contact-line email">e info@goldenhourstudio.net.au</p>
    </section>

    <div class="gold-rule upper"></div>
    <p class="slogan">moments held forever</p>
    <div class="gold-rule lower"></div>

    <div class="social-row">
      <span class="social-item">
        <svg class="social-dot" viewBox="0 0 52 52" aria-hidden="true">
          <defs>
            <linearGradient id="dotGold" x1="0" y1="0" x2="0" y2="1">
              <stop offset="0" stop-color="#b9862a"/>
              <stop offset="1" stop-color="#f0c01e"/>
            </linearGradient>
          </defs>
          <circle cx="26" cy="26" r="26" fill="url(#dotGold)"/>
        </svg>
        goldenhourbridals
      </span>
      <span class="social-item">
        <svg class="social-dot" viewBox="0 0 52 52" aria-hidden="true">
          <circle cx="26" cy="26" r="26" fill="url(#dotGold)"/>
        </svg>
        goldenhourbridals
      </span>
    </div>

    <p class="website">www.goldenhourstudio.net.au</p>
  </div>
</body>
</html>
```